Web Design Project

8 page static website.
About us/What we stand for:
Forno Lucente CBD plans to make a huge splash in Sydney by being the first Italian pizza and pasta retail food outlet offering truly fresh, nutritious ingredients – herbs and vegetables are picked directly from the garden, pizzas are made with love in a fun filled atmosphere and a cutting edge brand strategy that promotes a happy lifestyle and reminds people that happiness and togetherness comes from sharing amazing food.
The best thing about Forno Lucente is that it offers consumers a choice to either choose from the enticing gluten free and vegetarian menu range to the more traditional pizza and pasta, we cater for their own tastes, this provides a distinct point of difference in the retail food market, as well as allowing consumers to have an endless range of choices without having to worry about the nutritional value.
Consumers have now become accustomed to a consistent brand experience which is setting increasingly high standards when it comes to food quality, taste and service.
We want to capitalise on the opportunity to create a strong, modern brand that promotes healthy lifestyle habits, sells fresh, wholesome ingredients, delivers
exceptional service in a fun filled atmosphere and appeals to a broad market.
Our business model is specifically pickup and delivery with a few seats and crates for eating in. It is for the time poor that still want to have a great tasting Italian experience with pizza and pasta within the quick service restaurant space. Takeaway, office catering and delivery will be a large percentage of our business.
Our philosophy at Forno Lucente is simple:
“Success is not a formula, it’s a recipe”.
Brand personality:
We are located in a laneway and basically the shop is a hole in the one. It looks like a restaurant you would see in Italy.
Modern Italian, contemporary, fun, rustic (Taco Vela, Brasa’s)
1 Aims of this website
• Emotionally connect with the target audience to reflect (“happiness and togetherness comes from sharing amazing food”)
• To entice people to order pizza
• To capture a mailing list
• To differentiate us from the low cost, low quality pizza
• To create a connection with the target audience, and promote word of mouth
2 Target audience(s)
• Male/Female
• 18-49
• Sydney CBD and Woolloomooloo
• Internet Savvy.
3. Contents/Functionality
www.crustwagon.com.au – like the rustic brown in the website and the old washed out white colour through the font.
Target Market(s)
18-49 years old
City worker and resident
people that enjoy good food
Industry/Entity Type
Restaurant
Requirements
Must have
- Some splash of red and green to represent the italian theme.
Attached is a draft of the homepage layout.
Attached below are some fonts that we like.
Nice to have
- Please see http://www.brasashop.com.au/Pages/locationmenu.aspx
This is how our takeaway menu looks like.

```html
<!DOCTYPE html>
<html lang="en">
<head>
<meta charset="utf-8">
<title>Forno Lucente – Caffe Pizzeria</title>
<link href="https://fonts.googleapis.com/css2?family=Yanone+Kaffeesatz:wght@400;600&family=Fredoka:wght@600&family=Signika:wght@700&display=swap" rel="stylesheet">
<style>
:root{
  --bg-dark:#4f3b2a;
  --bg-mid:#6b5440;
  --panel:#b7a48a;
  --panel-light:#cbbba3;
  --card:#c2b095;
  --brown-deep:#5e3a24;
  --brown-btn:#6a3416;
  --red:#d8101c;
  --red-dark:#a50b12;
  --cream:#f4ede2;
  --white:#ffffff;
  --ink:#2b1e14;
  --green:#3d8b3a;
}
*{margin:0;padding:0;box-sizing:border-box}
html,body{width:1200px;height:1140px;overflow:hidden}
body{position:relative;background:radial-gradient(ellipse at 50% 40%,var(--bg-mid),var(--bg-dark) 80%);font-family:Arial,Helvetica,sans-serif;color:var(--ink)}
.abs{position:absolute}
.site-header{left:0;top:0;width:1200px;height:130px;background:var(--white)}
.brand-mark{left:42px;top:14px;width:190px;height:190px;border-radius:50%;background:var(--white);border:4px solid #9a9a9a;display:flex;align-items:center;justify-content:center;z-index:5}
.brand-mark span{font-family:"Yanone Kaffeesatz",sans-serif;font-weight:600;font-size:36px;color:var(--green);text-align:center;line-height:1}
.main-nav{left:271px;top:59px;display:flex;align-items:center;font-size:15px;color:#222}
.main-nav .home{background:var(--brown-btn);color:var(--white);width:72px;height:39px;border-radius:4px;display:flex;align-items:center;justify-content:center;margin-right:35px}
.main-nav .item{margin-right:44px}
.main-nav .item::before{content:"";display:inline-block;width:7px;height:7px;border-radius:50%;background:var(--brown-deep);margin-right:4px;vertical-align:1px}
.social-top{right:16px;top:10px;display:flex;gap:9px}
.dot{width:34px;height:34px;border-radius:50%;background:#2c6fb3}
.dot.alt{background:#e46a1b}
.content-panel{left:48px;top:132px;width:1098px;height:534px;border-radius:16px;background:var(--panel)}
.hero{left:61px;top:150px;width:799px;height:271px;border-radius:14px;overflow:hidden;background:linear-gradient(100deg,#c9552a,#b46a3a 40%,#e0b67a 70%,#d9a460)}
.hero-copy{right:28px;top:20px;text-align:center;font-family:Signika,sans-serif;font-weight:700;font-size:29px;line-height:35px;color:var(--white);-webkit-text-stroke:1px #222;text-shadow:2px 2px 0 #222}
.hero-copy em{font-style:normal;color:var(--red)}
.badge-new{width:74px;height:74px;border-radius:50%;background:var(--red);border:3px dashed var(--white);display:flex;align-items:center;justify-content:center;color:var(--white);font-family:Signika,sans-serif;font-size:17px}
.hero .badge-new{left:132px;top:14px}
.hero-from{left:138px;top:126px;font-family:Signika,sans-serif;font-weight:700;font-size:28px;color:var(--white);text-shadow:2px 2px 0 #222}
.hero-price{left:150px;top:160px;font-family:Fredoka,sans-serif;font-weight:600;font-size:74px;color:var(--red);-webkit-text-stroke:2px var(--white);line-height:1}
.hero-price small{font-size:30px}
.hero-each{right:36px;top:209px;font-family:Signika,sans-serif;font-size:21px;color:var(--white);text-shadow:1px 1px 0 #222}
.watch-ad{left:13px;top:221px;width:120px;height:39px;border-radius:6px;background:var(--brown-deep);color:var(--white);font-size:13px;display:flex;align-items:center;justify-content:center}
.order-cloud{left:886px;top:70px;width:230px;height:182px}
.order-text{left:914px;top:130px;font-family:Arial,sans-serif;font-weight:700;font-size:24px;color:var(--red);-webkit-text-stroke:1px var(--white);line-height:32px;white-space:nowrap}
.order-text span{display:block;padding-left:58px}
.about-card{left:884px;top:264px;width:242px;height:380px;border-radius:8px;background:var(--card);border:1px solid #8b7760;padding:18px 12px}
.about-photo{width:210px;height:134px;background:radial-gradient(circle,#e08a3a,#b8442a 70%,#8d5a34)}
.about-card h3{font-family:"Yanone Kaffeesatz",sans-serif;font-weight:400;font-size:31px;color:var(--ink);margin-top:8px}
.about-card p{font-family:"Yanone Kaffeesatz",sans-serif;font-size:19px;line-height:29px;color:var(--ink)}
.about-card p strong{font-weight:400;font-size:25px;color:#8c1a14}
.email-club{left:60px;top:445px;width:391px;height:203px;border-radius:14px;background:linear-gradient(var(--panel-light),#8a7055 75%,#6d5440);padding-top:14px}
.email-club h2{font-family:"Yanone Kaffeesatz",sans-serif;font-weight:400;font-size:30px;text-align:center;color:var(--ink)}
.field{display:flex;align-items:center;justify-content:flex-end;width:296px;margin-top:14px;font-size:15px;font-weight:bold;color:var(--white)}
.field .box{width:176px;height:28px;background:var(--white);border:1px solid #999;margin-left:8px}
.submit{display:block;margin:15px 0 0 125px;width:112px;height:37px;border-radius:5px;background:linear-gradient(var(--red),var(--red-dark));color:var(--white);font-family:"Yanone Kaffeesatz",sans-serif;font-size:21px;text-align:center;line-height:37px}
.catering{left:478px;top:443px;width:391px;height:204px;border-radius:12px;background:#0d0d0d}
.cans{left:10px;top:20px;width:150px;height:174px;background:linear-gradient(90deg,#b3121a,#e52b2b 40%,#7d0f15)}
.catering-title{left:172px;top:20px;font-family:"Yanone Kaffeesatz",sans-serif;font-weight:400;font-size:34px;color:var(--white)}
.catering-desc{left:172px;top:80px;font-family:Fredoka,sans-serif;font-weight:600;font-size:16px;line-height:19px;color:var(--red)}
.catering .badge-new{left:105px;top:120px}
.cater-price{left:212px;top:128px;font-family:Fredoka,sans-serif;font-weight:600;font-size:56px;line-height:1;color:var(--red);-webkit-text-stroke:2px var(--white)}
.cater-price small{font-size:26px}
.tile{top:707px;width:320px;height:218px;border-radius:5px;background:#bfa98a;padding:6px}
.tile .photo{width:100%;height:100%}
.tile-label{font-family:"Yanone Kaffeesatz",sans-serif;font-weight:600;font-size:30px;color:var(--red);-webkit-text-stroke:1px var(--white);line-height:44px}
.tile-order{left:46px}
.tile-order .photo{background:linear-gradient(#dcdad6,#a9a39a)}
.tile-order .tile-label{left:26px;top:116px}
.tile-catering{left:426px}
.tile-catering .photo{background:linear-gradient(#bdb8b0,#6e6a66)}
.tile-catering .tile-label{left:68px;top:116px}
.tile-delivery{left:820px;background:linear-gradient(#6d4a30,#a48768 60%,#c5b294)}
.tile-delivery .photo{position:absolute;left:20px;top:0;width:115px;height:218px;background:linear-gradient(#c9302c 40%,#2b3b55 60%)}
.tile-delivery .tile-label{left:152px;top:118px}
.footer-rule{left:52px;top:967px;width:1096px;height:2px;background:#7d6650}
.cards{left:56px;top:994px;display:flex;gap:4px}
.cards span{width:51px;height:28px;background:var(--white);border:1px solid #ccc}
.social-foot{left:72px;top:1056px;display:flex;gap:12px}
.social-foot .dot{width:32px;height:32px}
.foot-links{left:444px;top:1006px;font-size:13px;color:var(--cream)}
.copyright{left:535px;top:1053px;font-size:13px;color:var(--cream)}
.address{left:1001px;top:991px;font-size:13px;line-height:30px;color:var(--cream)}
.address b{font-weight:normal;font-size:16px}
</style>
</head>
<body>
<header class="site-header abs">
  <nav class="main-nav abs">
    <span class="home">HOME</span>
    <span class="item">ABOUT US</span>
    <span class="item">MENU</span>
    <span class="item">CONTACT US</span>
  </nav>
  <div class="social-top abs"><span class="dot"></span><span class="dot"></span><span class="dot"></span><span class="dot alt"></span></div>
</header>
<div class="brand-mark abs"><span>Forno<br>Lucente</span></div>

<div class="content-panel abs"></div>

<section class="hero abs" role="img" aria-label="Close-up photo of a loaded pizza with peppers, olives and mushrooms">
  <div class="badge-new abs">NEW</div>
  <p class="hero-copy abs">TRY <em>Chicken</em> &amp; Feta,<br>Creamy Chicken &amp; Cherry Tomato<br>Or BBQ <em>Chicken</em> &amp; Bacon</p>
  <p class="hero-from abs">From</p>
  <p class="hero-price abs"><small>$</small>8.95</p>
  <p class="hero-each abs">EACH PICK UP</p>
  <a class="watch-ad abs">WATCH THE AD &gt;</a>
</section>

<svg class="order-cloud abs" viewBox="0 0 230 182">
  <path d="M30 160 C0 150 2 100 14 80 C8 35 70 14 110 26 C150 0 218 14 214 66 C234 92 230 164 190 172 C150 186 70 182 30 160Z" fill="#5e3a24" stroke="#fff" stroke-width="7"/>
  <circle cx="122" cy="24" r="10" fill="#c7c22a"/>
</svg>
<p class="order-text abs">ORDER NOW<span>90415520</span></p>

<aside class="about-card abs">
  <div class="about-photo" role="img" aria-label="Photo of a pepperoni pizza with a slice being lifted"></div>
  <h3>At Forno Lucente,</h3>
  <p>we have perfected the secret to fresh, authentic <strong>Italian pizza.</strong> Made only from the highest quality and freshest natural ingredients, enjoy the ultimate pizza experience.</p>
</aside>

<section class="email-club abs">
  <h2>JOIN OUR EMAIL CLUB</h2>
  <div class="field">Name :<span class="box"></span></div>
  <div class="field">Email :<span class="box"></span></div>
  <span class="submit">Submit</span>
</section>

<section class="catering abs">
  <div class="cans abs" role="img" aria-label="Photo of two red soft drink cans"></div>
  <h3 class="catering-title abs">Corporate Catering</h3>
  <p class="catering-desc abs">3 chicken strips, chips<br>&amp; 375 ml can</p>
  <div class="badge-new abs">NEW</div>
  <p class="cater-price abs"><small>$</small>7.95</p>
</section>

<a class="tile tile-order abs"><div class="photo" role="img" aria-label="Photo of a smiling office worker at a laptop giving a thumbs up"></div><span class="tile-label abs">Click here to<br>Order Online</span></a>
<a class="tile tile-catering abs"><div class="photo" role="img" aria-label="Photo of colleagues sharing pizza at an office table"></div><span class="tile-label abs">Office Catering</span></a>
<a class="tile tile-delivery abs"><div class="photo" role="img" aria-label="Photo of a delivery driver in red carrying a pizza bag"></div><span class="tile-label abs">Delivery Area</span></a>

<footer>
  <div class="footer-rule abs"></div>
  <div class="cards abs"><span></span><span></span><span></span><span></span><span></span><span></span></div>
  <div class="social-foot abs"><span class="dot"></span><span class="dot"></span><span class="dot"></span><span class="dot alt"></span></div>
  <p class="foot-links abs">Home | Menu | Voucher | Store Finder | Corporate | Franchise | Contact Us</p>
  <p class="copyright abs">Copyright © FornoLucente,All Rights Reserved</p>
  <p class="address abs"><b>Address</b><br>Cotter Lane,<br>Sydney CBD NSW</p>
</footer>
</body>
</html>
```